Escape Room Flyer Design - Start up. A5

Flyer is for letterbox drops to get interest and let people know that our business exists and to a lesser extent what an escape room is. We have 1 room (the miller's shadows) and a second room coming soon (Varuna's Vault). I have attached our logo and 2 flyers that I have seen in the past that I really like the design of.
Whether you are having a night out with friends or family, celebrating a special event, planning a team-building activity, or simply wanting a diversion from the doldrums of your workweek, The Lock Box will provide you an unforgettable live-action gaming experience.

Target Market(s)

18-25

Industry/Entity Type

Entertainment

Requirements
Must have
• Logo. Phone number 0417 265 839. Website. www.thelockboxhartwell.com
Bookings essential.
Nice to have
• Mystery, a little bit on the darker side than bright colourful and blocky.
"Many Will Enter…Few Will Escape" tag line
60 minute game. Team work. 2-6 players. All ages.
Should not have
• Cartoons, characters, people

```html
<!DOCTYPE html>
<html lang="en">
<head>
<meta charset="utf-8">
<title>The Lock Box – A5 Flyer</title>
<link rel="stylesheet" href="https://fonts.googleapis.com/css2?family=Arimo:ital,wght@0,400;0,700;1,400&display=swap">
<style>
  :root {
    --page-bg: #ececec;
    --flyer-dark: #1c1c1c;
    --flyer-mid: #555555;
    --shade-black: #0e0e0e;
    --copper-deep: #c0621c;
    --copper-light: #f0a24c;
    --rule: #d07a2c;
    --text-light: #f4f4f4;
  }
  * { box-sizing: border-box; margin: 0; padding: 0; }
  html, body { width: 1200px; height: 849px; overflow: hidden; background: var(--page-bg); }
  .canvas { position: relative; width: 1200px; height: 849px; }
  .flyer {
    position: absolute; left: 304px; top: 0;
    width: 682px; height: 977px;
    transform: scale(0.869); transform-origin: top left;
    overflow: hidden;
    background: radial-gradient(ellipse 70% 60% at 50% 42%, var(--flyer-mid) 0%, #3a3a3a 45%, var(--flyer-dark) 100%);
    font-family: "Arimo", Arial, sans-serif;
    color: var(--text-light);
  }
  .flyer-art { position: absolute; inset: 0; width: 682px; height: 977px; }
  .motif {
    position: absolute;
    background: radial-gradient(circle at 50% 50%, var(--shade-black) 0%, rgba(14,14,14,0.85) 45%, rgba(14,14,14,0) 72%);
  }
  .motif-magnifier { left: -90px; top: -60px; width: 330px; height: 470px; }
  .motif-padlock { left: 540px; top: 300px; width: 220px; height: 280px; }
  .motif-keys { left: -110px; top: 720px; width: 420px; height: 300px; }
  .intro-title {
    position: absolute; left: 0; width: 682px; top: 421px;
    text-align: center; font-weight: 700; font-size: 19px;
  }
  .intro-copy {
    position: absolute; left: 131px; width: 420px; top: 461px;
    text-align: center; font-size: 14.4px; line-height: 18px;
  }
  .intro-copy em { font-style: italic; }
  .room-list {
    position: absolute; left: 0; width: 682px; top: 572px;
    text-align: center; font-size: 13px; font-weight: 700; color: var(--copper-light);
  }
  .game-facts {
    position: absolute; left: 124px; width: 434px; top: 620px; height: 46px;
    border-top: 2px solid var(--rule); border-bottom: 2px solid var(--rule);
    display: flex; align-items: center; justify-content: space-between;
    font-weight: 700; font-size: 16px; white-space: nowrap;
  }
  .contact { position: absolute; left: 126px; top: 730px; font-size: 12.5px; line-height: 23px; }
  .contact-row { display: flex; align-items: center; gap: 8px; }
  .contact-row svg { width: 15px; height: 15px; fill: var(--text-light); }
  .brand-name {
    position: absolute; left: 424px; width: 160px; top: 770px;
    text-align: center; font-weight: 700; font-size: 28px; line-height: 31px;
    color: var(--copper-light); letter-spacing: 1px;
  }
</style>
</head>
<body>
<div class="canvas">
  <article class="flyer">
    <div class="motif motif-magnifier" role="img" aria-label="Large dark magnifying glass silhouette"></div>
    <div class="motif motif-padlock" role="img" aria-label="Large dark padlock silhouette"></div>
    <div class="motif motif-keys" role="img" aria-label="Two large dark key silhouettes"></div>

    <svg class="flyer-art" viewBox="0 0 682 977" aria-hidden="true">
      <defs>
        <linearGradient id="copper" x1="0" y1="1" x2="1" y2="0">
          <stop offset="0" stop-color="var(--copper-light)"/>
          <stop offset="0.5" stop-color="var(--copper-deep)"/>
          <stop offset="1" stop-color="var(--copper-light)"/>
        </linearGradient>
        <linearGradient id="band" x1="0" y1="0" x2="1" y2="0">
          <stop offset="0" stop-color="#111"/>
          <stop offset="0.55" stop-color="#2a2a2a"/>
          <stop offset="0.75" stop-color="#5a5a5a"/>
          <stop offset="1" stop-color="#1a1a1a"/>
        </linearGradient>
        <path id="headline-top" d="M132 350 Q 300 232 546 246"/>
        <path id="headline-bottom" d="M168 382 Q 330 284 556 284"/>
      </defs>

      <polygon class="bookings-band" points="304,0 392,0 682,130 682,188" fill="url(#band)"/>
      <text x="524" y="90" transform="rotate(25.2 524 84)" text-anchor="middle"
            font-family="Arimo, Arial, sans-serif" font-weight="700" font-size="15" fill="#ffffff">BOOKINGS ESSENTIAL</text>

      <g font-family="Arimo, Arial, sans-serif" font-weight="700" fill="url(#copper)">
        <text font-size="38"><textPath href="#headline-top" textLength="430" lengthAdjust="spacing">MANY WILL ENTER...</textPath></text>
        <text font-size="38"><textPath href="#headline-bottom" textLength="400" lengthAdjust="spacing">...FEW WILL ESCAPE!</textPath></text>
      </g>
    </svg>

    <h1 class="intro-title">THE LOCK BOX ESCAPE ROOM</h1>
    <p class="intro-copy">Whether you are having a night out with friends or family, celebrating a special event, planning a team-building activity, or simply wanting a diversion from the doldrums of your workweek, <em>The Lock Box</em> will provide you an unforgettable live-action gaming experience.</p>
    <p class="room-list">Now playing: The Miller's Shadows &nbsp;|&nbsp; Coming soon: Varuna's Vault</p>

    <div class="game-facts">
      <span>60 MIN GAME</span><span>|</span><span>2 - 6 PLAYERS</span><span>|</span><span>ALL AGES WELCOME</span>
    </div>

    <div class="contact">
      <div class="contact-row">
        <svg viewBox="0 0 24 24"><path d="M6.6 10.8a15.1 15.1 0 0 0 6.6 6.6l2.2-2.2a1 1 0 0 1 1-.25 11.4 11.4 0 0 0 3.6.57 1 1 0 0 1 1 1V20a1 1 0 0 1-1 1A17 17 0 0 1 3 4a1 1 0 0 1 1-1h3.5a1 1 0 0 1 1 1c0 1.25.2 2.45.57 3.57a1 1 0 0 1-.25 1z"/></svg>
        <span>0417 265 839</span>
      </div>
      <div class="contact-row">
        <svg viewBox="0 0 24 24"><path d="M12 2a10 10 0 1 0 0 20 10 10 0 0 0 0-20zm6.9 6h-2.9a15.6 15.6 0 0 0-1.4-3.6A8 8 0 0 1 18.9 8zM12 4c.8 1.2 1.5 2.5 1.9 4h-3.8c.4-1.5 1.1-2.8 1.9-4zM4.3 14a8 8 0 0 1 0-4h3.4a16 16 0 0 0 0 4zm.8 2h2.9c.3 1.3.8 2.5 1.4 3.6A8 8 0 0 1 5.1 16zM8 8H5.1a8 8 0 0 1 4.3-3.6C8.8 5.5 8.3 6.7 8 8zm4 12c-.8-1.2-1.5-2.5-1.9-4h3.8c-.4 1.5-1.1 2.8-1.9 4zm2.3-6H9.7a14 14 0 0 1 0-4h4.6a14 14 0 0 1 0 4zm.3 5.6c.6-1.1 1.1-2.3 1.4-3.6h2.9a8 8 0 0 1-4.3 3.6zM16.3 14a16 16 0 0 0 0-4h3.4a8 8 0 0 1 0 4z"/></svg>
        <span>www.thelockboxhartwell.com</span>
      </div>
    </div>

    <div class="brand-name">THE<br>LOCK<br>BOX</div>
  </article>
</div>
</body>
</html>
```